Agricultural Consulting Website

Provide a modern yet business like website for my new Agriculture Consulting Business in Australia called FenTrove. Whilst we are based in Australia we are targetting both domestic and international markets (especially in Asia). We are targetting corporate, small business, government and farmer clients. The design should compliment our logo also sourced through pixel guild. The webiste should be easy for me to keep updated on a regular basis without the need to go back to the designer.

Industry/Entity Type

Business

Requirements
Must have
• clean crisp feel
• be modern yet business like
• be able to be updated by myself easily

```html
<!DOCTYPE html>
<html lang="en">
<head>
<meta charset="utf-8">
<title>FenTrove — Agricultural Consulting</title>
<link rel="stylesheet" href="https://fonts.googleapis.com/css2?family=Open+Sans:wght@400;600;700&family=Arimo:wght@400;700&display=swap">
<style>
  :root {
    --green-light: #d9ee9a;
    --green-mid: #9cc94a;
    --green-deep: #5e9a1e;
    --brand-green: #6a9a17;
    --brown: #6e3706;
    --brown-dark: #5a2c04;
    --brown-panel: #8a4f1b;
    --brown-button: #6a3004;
    --footer: #1e130b;
    --footer-line: #3a2818;
    --text-light: #f4e9dc;
    --text-brown: #6a3a08;
    --white: #ffffff;
  }
  * { box-sizing: border-box; margin: 0; padding: 0; }
  html, body { width: 1200px; height: 1190px; overflow: hidden; }
  body {
    position: relative;
    font-family: "Open Sans", Arial, sans-serif;
    background: var(--footer);
  }
  .abs { position: absolute; }

  /* Header band */
  .header-band {
    left: 0; top: 0; width: 1200px; height: 551px;
    background:
      radial-gradient(ellipse 420px 300px at 600px 160px, #f3f9d4 0%, rgba(243,249,212,0) 70%),
      radial-gradient(ellipse 260px 300px at 60px 300px, #6fa22a 0%, rgba(111,162,42,0) 80%),
      radial-gradient(ellipse 260px 300px at 1140px 300px, #79aa2e 0%, rgba(121,170,46,0) 80%),
      linear-gradient(180deg, #c7e07e 0%, #a9cf55 55%, #b9dc62 100%);
  }
  .brand { left: 265px; top: 30px; display: flex; align-items: center; gap: 10px; }
  .brand-mark { width: 135px; height: 137px; background: var(--brown-dark); }
  .brand-name {
    font-family: "Open Sans", Arial, sans-serif; font-weight: 600;
    font-size: 44px; color: var(--brand-green); letter-spacing: -0.5px;
  }

  .main-nav { left: 630px; top: 31px; display: flex; height: 25px; align-items: center;
    font-family: "Arimo", Arial, sans-serif; font-size: 9.5px; color: var(--text-brown); }
  .main-nav a { color: inherit; text-decoration: none; position: absolute; white-space: nowrap; }
  .main-nav .active {
    left: 0; width: 71px; height: 25px; line-height: 25px; text-align: center;
    background: var(--brown-button); color: var(--white); font-weight: 700;
  }

  .intro { left: 630px; top: 82px; width: 330px; font-family: "Arimo", Arial, sans-serif; color: var(--text-brown); }
  .intro h1 { font-size: 15px; font-weight: 400; margin-bottom: 10px; }
  .intro h1 strong { color: var(--brand-green); font-size: 19px; font-weight: 700; }
  .intro p { font-size: 8.3px; line-height: 14px; margin-bottom: 14px; }

  .hero-slider { left: 265px; top: 208px; width: 695px; height: 288px; overflow: hidden; }
  .hero-photo {
    width: 100%; height: 100%;
    background:
      radial-gradient(ellipse 250px 120px at 150px 40px, #eef6f6 0%, rgba(238,246,246,0) 80%),
      linear-gradient(100deg, #b9d79a 0%, #93c03e 35%, #6ea41e 60%, #3f7a12 100%);
  }
  .slider-arrow { width: 26px; height: 26px; border-radius: 50%; background: rgba(255,255,255,0.45);
    display: flex; align-items: center; justify-content: center; top: 137px; }
  .slider-dots { left: 373px; top: 265px; display: flex; gap: 3px; }
  .slider-dots span { width: 8px; height: 8px; border-radius: 50%; background: var(--white); }
  .slider-dots span.current { background: var(--brown-button); }

  .search-field { left: 265px; top: 510px; width: 144px; height: 29px; background: var(--white);
    font-size: 10px; color: #999; padding: 8px 9px; }
  .search-field svg { position: absolute; right: 8px; top: 8px; }
  .signup { top: 510px; height: 29px; }
  .signup-label { left: 668px; top: 518px; font-size: 11px; color: var(--text-brown); padding-right: 10px; border-right: 1px solid #c89a6a; line-height: 12px; }
  .input-box { background: var(--white); font-size: 7px; color: #aaa; padding: 11px 9px; }
  .go-button { left: 928px; width: 31px; background: var(--brown-button); color: var(--white);
    font-size: 10px; font-weight: 700; text-align: center; line-height: 29px; }

  /* About band */
  .about-band { left: 0; top: 551px; width: 1200px; height: 502px;
    background: linear-gradient(180deg, #6f3805 0%, #77400a 60%, #7a420b 100%); color: var(--text-light); }
  .section-title { font-size: 17px; font-weight: 400; color: var(--white); }
  .section-sub { font-size: 10px; color: var(--white); }
  .about-photo { left: 265px; top: 109px; width: 219px; height: 109px;
    background: linear-gradient(90deg, #d8ecb6 0%, #9cc84a 40%, #7cae25 70%, #c7e07e 100%); }
  .body-copy { font-size: 7.7px; line-height: 11px; color: var(--text-light); }
  .rule { height: 1px; background: rgba(255,255,255,0.12); }

  .news-date { font-size: 7px; font-style: italic; color: var(--text-light); }
  .view-all-link { font-size: 7.5px; color: var(--white); text-decoration: underline; font-weight: 600; }

  .recent-posts { left: 653px; top: 269px; width: 306px; height: 200px; background: var(--brown-panel); }
  .light-button { left: 17px; top: 115px; width: 68px; height: 26px; background: linear-gradient(#ffffff, #d8d8d8);
    color: var(--brown-dark); font-size: 7.5px; font-weight: 700; text-align: center; line-height: 26px; }

  /* Footer */
  .site-footer { left: 0; top: 1053px; width: 1200px; height: 137px; background: var(--footer); color: #cbbfae; }
  .footer-title { font-size: 15px; color: var(--white); font-weight: 400; }
  .footer-links { list-style: none; font-size: 7.7px; line-height: 14.3px; }
  .footer-links a { color: #cbbfae; text-decoration: none; }
  .footer-links a.current { color: var(--white); text-decoration: underline; }
  .email-field { left: 468px; top: 86px; width: 132px; height: 24px; background: #5a4232;
    font-size: 8px; color: #b9a690; padding: 7px 7px; }
  .sign-in { left: 604px; top: 86px; width: 49px; height: 24px; background: #6b4a35;
    color: var(--white); font-size: 9.5px; text-align: center; line-height: 24px; }
  .footer-brand { left: 813px; top: 30px; display: flex; align-items: center; gap: 6px; }
  .footer-brand .brand-mark { width: 27px; height: 27px; background: #5a3a1a; }
  .footer-brand .brand-name { font-size: 18px; }
  .social { width: 21px; height: 20px; background: #8a4d12; top: 90px; }
</style>
</head>
<body>

<header class="abs header-band">
  <div class="abs brand">
    <div class="brand-mark"></div>
    <span class="brand-name">FenTrove</span>
  </div>

  <nav class="abs main-nav">
    <a class="active" href="#">Home</a>
    <a href="#" style="left:92px">About Us</a>
    <a href="#" style="left:158px">Events</a>
    <a href="#" style="left:215px">Activities</a>
    <a href="#" style="left:276px">Contact Us</a>
  </nav>

  <div class="abs intro">
    <h1>Lorem <strong>FenTrove</strong> dolor sit amet</h1>
    <p>Lorem ipsum dolor sit amet, consectetur adipisicing elit, sed do eiusmod tempor incidid-unt ut labore et dolore magna aliqua. Ut enim ad</p>
    <p>Minim veniam, quis nostrud exercitation ullamco laboris nisi ut aliquip</p>
  </div>

  <div class="abs hero-slider">
    <div class="hero-photo" role="img" aria-label="Close-up of green wheat ears in a sunny field"></div>
    <div class="abs slider-arrow" style="left:17px">
      <svg width="12" height="10" viewBox="0 0 12 10"><path d="M11 5H2M5 1L1 5l4 4" stroke="#fff" stroke-width="2" fill="none"/></svg>
    </div>
    <div class="abs slider-arrow" style="left:652px">
      <svg width="12" height="10" viewBox="0 0 12 10"><path d="M1 5h9M7 1l4 4-4 4" stroke="#fff" stroke-width="2" fill="none"/></svg>
    </div>
    <div class="abs slider-dots"><span class="current"></span><span></span><span></span><span></span></div>
  </div>

  <div class="abs search-field">Search
    <svg width="12" height="12" viewBox="0 0 12 12"><circle cx="5" cy="5" r="3.5" stroke="#bbb" stroke-width="1.3" fill="none"/><path d="M7.5 7.5L11 11" stroke="#bbb" stroke-width="1.5"/></svg>
  </div>
  <div class="abs signup-label">Sign Up</div>
  <div class="abs signup input-box" style="left:720px;width:101px">Username</div>
  <div class="abs signup input-box" style="left:825px;width:100px">Password</div>
  <div class="abs signup go-button">Go</div>
</header>

<main class="abs about-band">
  <h2 class="abs section-title" style="left:265px;top:40px">Lorem ipsum dolor sit amet</h2>
  <p class="abs section-sub" style="left:265px;top:77px">Lorem ipsum dolor sit amet</p>

  <div class="abs about-photo" role="img" aria-label="Green wheat stalks in close-up"></div>
  <p class="abs body-copy" style="left:499px;top:107px;width:461px">Lorem ipsum dolor sit amet, consectetur adipisicing elit, sed do eiusmod tempor incididunt ut labore et dolore magna aliqua. Ut enim ad minim veniam, quis nostrud exercitation ullamco laboris nisi ut aliquip ex ea commodo consequat. Duis aute irure dolor in reprehenderit in voluptate velit esse cillum dolore eu fugiat nulla pariatur. Excepteur sint occaecat cupidatat non proident, sunt in culpa qui officia deserunt mollit anim id est laborum.</p>
  <p class="abs body-copy" style="left:499px;top:178px;width:461px">Lorem ipsum dolor sit amet, consectetur adipisicing elit, sed do eiusmod tempor incididunt ut labore et dolore magna aliqua. Ut enim ad minim veniam, quis nostrud exercitation ullamco laboris nisi ut aliquip ex ea commodo consequat. Duis aute irure dolor in reprehenderit in voluptate velit esse cillum dolore eu fugiat nulla pariatur. Excepteur sint occaecat cupidatat non proident, sunt in culpa qui officia deserunt mollit anim id est laborum.</p>

  <div class="abs rule" style="left:265px;top:246px;width:695px"></div>

  <section>
    <h2 class="abs section-title" style="left:265px;top:290px">Latest Events &amp; News</h2>
    <p class="abs news-date" style="left:267px;top:330px">27 November 2013</p>
    <p class="abs body-copy" style="left:267px;top:345px;width:290px">Lorem ipsum dolor sit amet, consectetur adipisicing elit, sed do eiusmod tempor incididunt ut labore et dolore magna aliqua. Ut enim ad minim veniam, quis nostrud exercitation</p>
    <div class="abs rule" style="left:265px;top:388px;width:283px"></div>
    <p class="abs news-date" style="left:267px;top:398px">27 November 2013</p>
    <p class="abs body-copy" style="left:267px;top:413px;width:290px">Lorem ipsum dolor sit amet, consectetur adipisicing elit, sed do eiusmod tempor incididunt ut labore et dolore magna aliqua. Ut enim ad minim veniam, quis nostrud exercitation</p>
    <a class="abs view-all-link" style="left:266px;top:460px" href="#">VIEW ALL &gt;&gt;</a>
  </section>

  <section class="abs recent-posts">
    <h2 class="abs section-title" style="left:16px;top:21px">Recent Posts</h2>
    <p class="abs body-copy" style="left:17px;top:60px;width:280px">Lorem ipsum dolor sit amet, consectetur adipisicing elit, sed do eiusmod tempor incididunt ut labore et dolore magna aliqua. Ut enim ad minim veniam, quis nostrud exercitation ullamco laboris nisi ut aliquip ex ea commodo consequat.</p>
    <a class="abs light-button" href="#" style="text-decoration:none">VIEW ALL &gt;&gt;</a>
  </section>
</main>

<footer class="abs site-footer">
  <h3 class="abs footer-title" style="left:265px;top:25px">Links</h3>
  <ul class="abs footer-links" style="left:265px;top:50px">
    <li><a class="current" href="#">Home</a></li>
    <li><a href="#">About Us</a></li>
    <li><a href="#">Events</a></li>
    <li><a href="#">Activities</a></li>
    <li><a href="#">Contact Us</a></li>
  </ul>

  <h3 class="abs footer-title" style="left:468px;top:25px">Subscribe</h3>
  <p class="abs body-copy" style="left:468px;top:55px;width:195px;font-size:7px;color:#e8ddd0">Lorem ipsum dolor sit amet, consectetur adipisicing elit, sed do eiusmod tempor incididunt ut labore et dolore magna aliqua.</p>
  <div class="abs email-field">email@example.com</div>
  <div class="abs sign-in">Sign In</div>

  <div class="abs footer-brand">
    <div class="brand-mark"></div>
    <span class="brand-name">FenTrove</span>
  </div>
  <p class="abs" style="left:764px;top:69px;width:195px;text-align:center;font-size:6.5px;color:#9c8f80">All Right Reserved 2013.</p>
  <div class="abs rule" style="left:764px;top:86px;width:195px;background:var(--footer-line)"></div>
  <a class="abs social" style="left:831px" href="#" aria-label="Social link one"></a>
  <a class="abs social" style="left:856px" href="#" aria-label="Social link two"></a>
  <a class="abs social" style="left:880px" href="#" aria-label="Social link three"></a>
</footer>

</body>
</html>
```